Restaurant Menu Design for Meal Prep offered in a food display cooler at a local Gym

I am looking for a menu design with the following items . I would like a workable copy if possible so in the future we can change pricing on this file , or change items . This file will be uploaded on a USB drive and then plugged into a TV. Please ensure a JPEG file is included so this will also work on this TV.

Have a look at our website , www.quilvarkitchen.com for ideas for design that represent the brand appropriately.
The below are the menu items that we would need displayed along with their pricing.

BREAKFAST MEAL PREP ITEMS
Blueberry Pancakes $12.00
Copper Lantern Burrito $10.95

LUNCH/DINNER MEAL PREP OPTIONS
BBQ Glazed Salmon $16.50
Cheeseburger Bowl $13.50
Chicken Alfredo $12.00
Pesto Chicken Pasta $12.00
Chicken Parmesan $13.00
Taco Bowl $14.00
Steak Bite and Green Stir Fry $12.00
Asian Chicken Teriyaki $12.00
Marlowe Stir Fry $15.95

I will attach our logo below, this will need to be on the design. The "heading" (for example breakfast meal prep items and lunch/dinner meal prep options) for the menu should also be on the design.

Ive attached a couple of photos that you need to add to your design.

This will be displayed in a GYM

Meal Prep + Fitness Industry

• Quilvar Logo and Photos attached
• Maybe incorporate something that represents working out or healthy lifestyle in design without going too overboard

```html
<!DOCTYPE html>
<html lang="en">
<head>
<meta charset="UTF-8">
<title>Quilvar Healthy Kitchen – Meal Prep Menu</title>
<link href="https://fonts.googleapis.com/css2?family=Montserrat:wght@500;600;700;800&display=swap" rel="stylesheet">
<style>
  :root {
    --paper: #f8f8f6;
    --green: #9dbf2e;
    --green-deep: #86a821;
    --green-soft: #c9dc82;
    --grey-head: #8d8d8d;
    --grey-text: #6b6b6b;
    --white: #ffffff;
  }
  * { margin: 0; padding: 0; box-sizing: border-box; }
  html, body { width: 857px; height: 1200px; overflow: hidden; background: var(--paper); }
  body { font-family: 'Montserrat', sans-serif; }
  .menu { position: relative; width: 857px; height: 1200px; overflow: hidden; background: var(--paper); }
  .backdrop { position: absolute; inset: 0; }

  .brand { position: absolute; left: 67px; top: 362px; }
  .brand-name { font-size: 56px; font-weight: 800; color: var(--green); letter-spacing: 1px; line-height: 1; display: flex; align-items: center; gap: 10px; }
  .brand-dot { width: 14px; height: 14px; border-radius: 50%; background: var(--green); }
  .brand-tag { margin-top: 8px; margin-left: 11px; font-size: 16.5px; font-weight: 700; color: var(--green); letter-spacing: .2px; }

  .section-title { position: absolute; left: 91px; font-size: 27px; font-weight: 800; color: var(--grey-head); line-height: 34px; text-transform: uppercase; }
  .section-title::before { content: ""; position: absolute; left: -24px; top: 13px; width: 10px; height: 10px; border-radius: 50%; background: var(--grey-head); }

  .item { position: absolute; width: 340px; }
  .item-name { font-size: 19px; font-weight: 700; color: var(--green); line-height: 24px; white-space: nowrap; }
  .item-name.tight { letter-spacing: -0.9px; }
  .item-desc { margin-top: 4px; font-size: 11.4px; font-weight: 500; color: var(--grey-text); line-height: 14px; white-space: nowrap; }
  .item-desc.narrow { font-size: 10.6px; letter-spacing: -0.2px; }

  .delivery { position: absolute; left: 14px; top: 1096px; width: 275px; height: 72px; background: linear-gradient(90deg, var(--green-deep), var(--green)); border-radius: 0 10px 10px 0; border: 2px solid var(--green-soft); color: var(--white); }
  .delivery-title { position: absolute; left: 76px; top: 6px; font-size: 27px; font-weight: 800; letter-spacing: .5px; }
  .delivery-title::before { content: ""; position: absolute; left: -22px; top: 13px; width: 9px; height: 9px; border-radius: 50%; background: var(--white); }
  .delivery-phone { position: absolute; left: 76px; top: 43px; font-size: 15px; font-weight: 700; display: flex; align-items: center; gap: 8px; }
  .phone-icon { width: 21px; height: 21px; }
</style>
</head>
<body>
<main class="menu">
  <svg class="backdrop" width="857" height="1200" viewBox="0 0 857 1200" xmlns="http://www.w3.org/2000/svg">
    <defs>
      <linearGradient id="leafGreen" x1="0" y1="0" x2="1" y2="1">
        <stop offset="0" stop-color="#b2cb45"/>
        <stop offset="1" stop-color="#86a821"/>
      </linearGradient>
      <radialGradient id="pastaTone" cx=".55" cy=".55" r=".6">
        <stop offset="0" stop-color="#8fa25c"/>
        <stop offset=".45" stop-color="#a9ae7c"/>
        <stop offset=".6" stop-color="#f2f2f0"/>
        <stop offset="1" stop-color="#d6d9da"/>
      </radialGradient>
      <linearGradient id="trayTone" x1="0" y1="0" x2="1" y2="1">
        <stop offset="0" stop-color="#6f6a3c"/>
        <stop offset=".5" stop-color="#c88a54"/>
        <stop offset="1" stop-color="#3a302a"/>
      </linearGradient>
      <linearGradient id="pancakeTone" x1="0" y1="0" x2="1" y2="1">
        <stop offset="0" stop-color="#e4e6e7"/>
        <stop offset=".5" stop-color="#e8c99a"/>
        <stop offset="1" stop-color="#c9cdce"/>
      </linearGradient>
    </defs>

    <path d="M0,0 H440 C450,210 385,340 225,355 C130,363 50,345 0,325 Z" fill="url(#leafGreen)"/>
    <path role="img" aria-label="Photo: stack of protein pancakes with blueberries and yogurt drizzle on a white plate" d="M0,0 H382 C392,125 330,250 190,262 C110,268 45,245 0,218 Z" fill="url(#pancakeTone)"/>

    <path d="M400,0 H857 V602 C760,608 640,575 560,530 C470,475 430,390 420,280 C412,180 405,80 400,0 Z" fill="url(#leafGreen)"/>
    <circle cx="665" cy="290" r="248" fill="var(--white)"/>
    <circle role="img" aria-label="Photo: bowl of pesto chicken penne with broccoli, peppers and parmesan" cx="665" cy="290" r="236" fill="url(#pastaTone)"/>

    <circle cx="-8" cy="600" r="80" fill="url(#leafGreen)"/>
    <circle cx="872" cy="898" r="52" fill="url(#leafGreen)"/>
    <circle cx="318" cy="1208" r="40" fill="var(--green-soft)" opacity=".55"/>

    <circle cx="720" cy="1250" r="325" fill="url(#leafGreen)"/>
    <circle cx="720" cy="1250" r="272" fill="var(--white)"/>
    <circle role="img" aria-label="Photo: meal prep containers with chicken, rice, vegetables and baked pasta" cx="720" cy="1250" r="262" fill="url(#trayTone)"/>
  </svg>

  <header class="brand">
    <div class="brand-name"><span class="brand-dot"></span>QUILVAR</div>
    <div class="brand-tag">HEALTHY KITCHEN &nbsp;|&nbsp; MEAL PREP</div>
  </header>

  <h2 class="section-title" style="top:464px;">Breakfast Meal<br>Prep Items</h2>

  <div class="item" style="left:91px; top:546px;">
    <div class="item-name">Blueberry Pancakes ....... $12.00</div>
    <div class="item-desc narrow">Gluten free protein pancake mix, fresh blueberries, blue-<br>berry yogurt sauce, served with 100% maple syrup.</div>
  </div>
  <div class="item" style="left:91px; top:608px;">
    <div class="item-name tight">Copper Lantern Burrito .. $10.95</div>
    <div class="item-desc">Lorem Ipsum is simply dummy text of the printing<br>and typesetting industry.</div>
  </div>

  <h2 class="section-title" style="top:678px;">Lunch/Dinner Meal<br>Prep Options</h2>

  <div class="item" style="left:91px; top:767px;">
    <div class="item-name">BBQ Glazed Salmon ....... $16.50</div>
    <div class="item-desc">Lorem Ipsum is simply dummy text of the printing<br>and typesetting industry.</div>
  </div>
  <div class="item" style="left:91px; top:829px;">
    <div class="item-name">Cheeseburger Bowl ........ $13.50</div>
    <div class="item-desc">Lorem Ipsum is simply dummy text of the printing<br>and typesetting industry.</div>
  </div>
  <div class="item" style="left:91px; top:892px;">
    <div class="item-name">Chicken Alfredo ............... $12.00</div>
    <div class="item-desc">Lorem Ipsum is simply dummy text of the printing<br>and typesetting industry.</div>
  </div>
  <div class="item" style="left:91px; top:955px;">
    <div class="item-name">Pesto Chicken Pasta ...... $12.00</div>
    <div class="item-desc">Lorem Ipsum is simply dummy text of the printing<br>and typesetting industry.</div>
  </div>
  <div class="item" style="left:91px; top:1018px;">
    <div class="item-name">Chicken Parmesan ......... $13.00</div>
    <div class="item-desc">Lorem Ipsum is simply dummy text of the printing<br>and typesetting industry.</div>
  </div>

  <div class="item" style="left:487px; top:669px;">
    <div class="item-name">Taco Bowl ............................ $14.00</div>
    <div class="item-desc">Lorem Ipsum is simply dummy text of the printing<br>and typesetting industry.</div>
  </div>
  <div class="item" style="left:487px; top:739px;">
    <div class="item-name tight">Steak Bite and Green Stir Fry ... $12.00</div>
    <div class="item-desc">Lorem Ipsum is simply dummy text of the printing<br>and typesetting industry.</div>
  </div>
  <div class="item" style="left:487px; top:808px;">
    <div class="item-name">Asian Chicken Teriyaki ... $12.00</div>
    <div class="item-desc">Lorem Ipsum is simply dummy text of the printing<br>and typesetting industry.</div>
  </div>
  <div class="item" style="left:487px; top:877px;">
    <div class="item-name">Marlowe Stir Fry ............. $15.95</div>
    <div class="item-desc">Lorem Ipsum is simply dummy text of the printing<br>and typesetting industry.</div>
  </div>

  <aside class="delivery">
    <div class="delivery-title">DELIVERY</div>
    <div class="delivery-phone">
      <svg class="phone-icon" viewBox="0 0 24 24" aria-hidden="true">
        <circle cx="12" cy="12" r="12" fill="#ffffff"/>
        <path d="M8.2 5.8c.4-.3 1-.2 1.3.2l1.4 2.1c.3.4.2 1-.1 1.3l-.9.8c.6 1.5 1.8 2.8 3.3 3.5l.8-.9c.3-.4.9-.5 1.3-.2l2.1 1.3c.4.3.6.9.3 1.3l-.7 1.1c-.5.8-1.5 1.1-2.4.8-3.6-1.2-6.3-4-7.4-7.6-.3-.9.1-1.9.9-2.4z" fill="#8fb02a"/>
      </svg>
      +0 123 456 789
    </div>
  </aside>
</main>
</body>
</html>
```